Pre-Paid Card for Teens needs a design

We are a Fintech company called Velorant. We will sell prepaid cards for families and teens. Now we need a prepaid card design. Prepaid card should have a paywheel logo, company logo, 16 card number, expire date. Our webpage is http://www.velorant-example.com
Target Market(s)
Teenages between 8 - 18 years old
Industry/Entity Type
It Company
Requirements
Must have
- The prepaid card must include velorant logo, paywheel debit card logo (I already attached a sample card), 16 digit card number and expire date.
Nice to have
- It should be fun and prestigious for young people.
Should not have
- We don't want that the card has a lots of color

```html
<!DOCTYPE html>
<html lang="en">
<head>
<meta charset="utf-8">
<title>Velorant Prepaid Card</title>
<link href="https://fonts.googleapis.com/css2?family=Montserrat:wght@500;600;700&family=Share+Tech+Mono&display=swap" rel="stylesheet">
<style>
  :root {
    --card-bg: #230b45;
    --band: #3f1a63;
    --brand-orange: #f0a020;
    --silver: #d9d9de;
    --silver-dark: #8d8d98;
    --gold: #f7c21a;
    --chip-light: #f3dd94;
    --chip-dark: #c9a24c;
    --chip-line: #7a5d22;
    --page-bg: #ffffff;
  }
  html, body {
    margin: 0;
    padding: 0;
    width: 1200px;
    height: 777px;
    overflow: hidden;
    background: var(--page-bg);
  }
  .card {
    position: relative;
    width: 1200px;
    height: 777px;
    background: var(--card-bg);
    border-radius: 48px;
    overflow: hidden;
    font-family: "Montserrat", sans-serif;
  }
  .card-bands {
    position: absolute;
    inset: 0;
  }
  .brand-logo {
    position: absolute;
    left: 58px;
    top: 28px;
    margin: 0;
    font-weight: 700;
    font-size: 60px;
    letter-spacing: 2px;
    color: var(--brand-orange);
  }
  .chip {
    position: absolute;
    left: 57px;
    top: 301px;
    width: 114px;
    height: 106px;
  }
  .card-number {
    position: absolute;
    left: 57px;
    top: 436px;
    font-family: "Share Tech Mono", monospace;
    font-size: 44px;
    letter-spacing: 9px;
    word-spacing: 10px;
    color: var(--silver);
    text-shadow: 1px 1px 0 var(--silver-dark);
    white-space: nowrap;
  }
  .card-code {
    position: absolute;
    left: 57px;
    top: 486px;
    font-size: 25px;
    font-weight: 500;
    color: var(--silver);
  }
  .date-block {
    position: absolute;
    top: 536px;
    color: var(--silver);
    font-weight: 500;
  }
  .date-block.valid { left: 57px; }
  .date-block.expires { left: 327px; }
  .date-label {
    font-size: 25px;
    letter-spacing: 1px;
  }
  .date-value {
    font-size: 27px;
    margin-top: 14px;
  }
  .holder-name {
    position: absolute;
    left: 60px;
    top: 640px;
    font-size: 52px;
    font-weight: 600;
    letter-spacing: 6px;
    color: var(--gold);
    white-space: nowrap;
  }
  .payment-marks {
    position: absolute;
    right: 44px;
    bottom: 44px;
    display: flex;
    align-items: center;
    gap: 18px;
  }
  .payment-mark {
    font-weight: 700;
    font-size: 28px;
    color: var(--silver);
  }
  .payment-mark.paywheel {
    display: flex;
    align-items: center;
    gap: 8px;
  }
  .payment-mark.paywheel .dot {
    width: 26px;
    height: 26px;
    border-radius: 50%;
    background: var(--silver);
  }
</style>
</head>
<body>
  <div class="card">
    <svg class="card-bands" width="1200" height="777" viewBox="0 0 1200 777" aria-hidden="true">
      <path d="M760 0 L1200 0 L1200 120 Q1000 90 700 190 Z" fill="var(--band)"/>
      <path d="M300 777 Q560 700 900 640 L800 777 Z" fill="var(--band)"/>
    </svg>

    <h1 class="brand-logo">velorant</h1>

    <svg class="chip" viewBox="0 0 114 106" aria-hidden="true">
      <defs>
        <linearGradient id="chipGold" x1="0" y1="0" x2="1" y2="1">
          <stop offset="0" stop-color="var(--chip-light)"/>
          <stop offset="1" stop-color="var(--chip-dark)"/>
        </linearGradient>
      </defs>
      <rect x="0" y="0" width="114" height="106" rx="16" fill="url(#chipGold)"/>
      <g stroke="var(--chip-line)" stroke-width="2" fill="none">
        <path d="M0 30 H36 M0 54 H36 M0 76 H36 M36 0 V76"/>
        <path d="M78 0 V106 M78 30 H114 M78 54 H114 M78 76 H114"/>
      </g>
    </svg>

    <div class="card-number">9094 6206 0000 0157</div>
    <div class="card-code">4985</div>

    <div class="date-block valid">
      <div class="date-label">VALID FROM</div>
      <div class="date-value">04/12</div>
    </div>
    <div class="date-block expires">
      <div class="date-label">EXPIRES END</div>
      <div class="date-value">04/16</div>
    </div>

    <div class="holder-name">JORDAN REYES</div>

    <div class="payment-marks">
      <span class="payment-mark cardvia">Cardvia</span>
      <span class="payment-mark paywheel"><span class="dot"></span>paywheel</span>
    </div>
  </div>
</body>
</html>
```